Tidewell Care Community Catalogue

I would like an A4 brochure designed consistent with my company branding . This can be seen at www.tidewellcare.com.au . All content is available in document below.

I've also included the brand guidelines document.

Target Market(s)

People in the community suffering from injuries & Disabilities

Industry/Entity Type

Health Service

Font styles to use

Colors
33b8a4
acd037

Requirements
Must have
• Good use of the pictures I've included.
• Brand colours & Fonts
• Consistency with brand look and feel

```html
<!DOCTYPE html>
<html lang="en">
<head>
<meta charset="utf-8">
<title>Tidewell Care Community Catalogue – Cover Options</title>
<link rel="stylesheet" href="https://fonts.googleapis.com/css2?family=Montserrat:wght@300;400;500;600&display=swap">
<style>
  :root {
    --backdrop: #a4612b;
    --paper: #ffffff;
    --paper-grey: #e9e9e9;
    --forest: #1d6a46;
    --forest-deep: #174f37;
    --forest-photo-a: #2b6b4c;
    --forest-photo-b: #143f2c;
    --lime: #acd037;
    --teal: #33b8a4;
    --ink: #1e3f4a;
    --ink-soft: #444b50;
    --label: #f6efe6;
  }
  * { box-sizing: border-box; margin: 0; padding: 0; }
  html, body { width: 1200px; height: 900px; overflow: hidden; }
  body {
    background: var(--backdrop);
    font-family: "Montserrat", sans-serif;
    position: relative;
  }
  .cover {
    position: absolute;
    top: 80px;
    width: 468px;
    height: 655px;
    overflow: hidden;
    box-shadow: 0 6px 18px rgba(0,0,0,.35);
  }
  .cover--option-3 { left: 70px; background: var(--paper-grey); }
  .cover--option-4 { left: 634px; background: var(--paper); }
  .cover svg.cover__art { position: absolute; inset: 0; width: 100%; height: 100%; }

  .wordmark {
    position: absolute;
    font-weight: 300;
    text-transform: uppercase;
    letter-spacing: .06em;
    white-space: nowrap;
    display: flex;
    align-items: center;
    gap: 10px;
  }
  .wordmark__square { width: 14px; height: 14px; background: var(--teal); }
  .cover--option-3 .wordmark { top: 70px; left: 200px; font-size: 24px; color: var(--ink-soft); }
  .cover--option-4 .wordmark {
    top: 138px; left: 0; right: 0; justify-content: center;
    font-size: 30px; color: var(--ink-soft);
  }

  .cover__web {
    position: absolute;
    font-size: 13px;
    letter-spacing: .01em;
  }
  .cover--option-3 .cover__web { left: 134px; bottom: 26px; color: var(--paper); font-size: 14px; }
  .cover--option-4 .cover__web { right: 30px; bottom: 20px; color: var(--ink); font-size: 11.5px; }

  .cover__questions {
    position: absolute;
    top: 224px; left: 30px; right: 33px;
    text-align: center;
    font-size: 10.6px;
    font-weight: 500;
    line-height: 1.55;
    color: var(--ink);
    text-transform: uppercase;
  }

  .option-label {
    position: absolute;
    top: 770px;
    width: 468px;
    text-align: center;
    font-size: 27px;
    font-weight: 500;
    color: var(--label);
    letter-spacing: .01em;
  }
  .option-label--3 { left: 50px; }
  .option-label--4 { left: 646px; }
</style>
</head>
<body>

  <section class="cover cover--option-3">
    <svg class="cover__art" viewBox="0 0 468 655" preserveAspectRatio="none" aria-hidden="false">
      <defs>
        <linearGradient id="photoToneA" x1="0" y1="0" x2="1" y2="1">
          <stop offset="0" stop-color="var(--forest-photo-a)"/>
          <stop offset="1" stop-color="var(--forest-photo-b)"/>
        </linearGradient>
      </defs>
      <polygon points="0,85 270,332 468,200 468,655 0,655" fill="url(#photoToneA)"
               role="img" aria-label="Photo of a therapist demonstrating equipment, toned green"/>
      <polygon points="0,85 270,332 0,332" fill="var(--forest)" opacity=".55"/>
      <line x1="72" y1="110" x2="378" y2="365" stroke="#111" stroke-width="1.2"/>
      <line x1="262" y1="258" x2="466" y2="432" stroke="#111" stroke-width="1.2"/>
      <line x1="66" y1="470" x2="330" y2="340" stroke="var(--forest)" stroke-width="7" opacity=".8"/>
      <line x1="130" y1="570" x2="468" y2="575" stroke="var(--forest)" stroke-width="6" opacity=".6"/>
      <polygon points="227,157 302,230 227,230" fill="var(--lime)"/>
      <polygon points="263,240 308,240 282,280" fill="var(--teal)"/>
    </svg>
    <div class="wordmark"><span class="wordmark__square"></span>Tidewell Care</div>
    <p class="cover__web">www.tidewellcare.com.au</p>
  </section>

  <section class="cover cover--option-4">
    <svg class="cover__art" viewBox="0 0 468 655" preserveAspectRatio="none">
      <defs>
        <linearGradient id="photoToneB" x1="0" y1="0" x2="1" y2="1">
          <stop offset="0" stop-color="var(--forest-photo-a)"/>
          <stop offset="1" stop-color="var(--forest-photo-b)"/>
        </linearGradient>
      </defs>
      <rect x="30" y="25" width="405" height="262" fill="none" stroke="var(--ink)" stroke-width="2"/>
      <line x1="108" y1="206" x2="355" y2="206" stroke="var(--ink-soft)" stroke-width="1"/>
      <rect x="0" y="285" width="468" height="316" fill="url(#photoToneB)"
            role="img" aria-label="Photo of a therapist demonstrating equipment, toned green"/>
      <line x1="92" y1="285" x2="370" y2="460" stroke="var(--forest-deep)" stroke-width="5" opacity=".8"/>
      <polygon points="468,438 468,601 300,601" fill="var(--paper)"/>
      <polygon points="436,418 436,576 296,576" fill="var(--lime)"/>
    </svg>
    <div class="wordmark"><span class="wordmark__square"></span>Tidewell Care</div>
    <p class="cover__questions">Where include home services, eg gardening?<br>Where for initial accident assessment?</p>
    <p class="cover__web">www.tidewellcare.com.au</p>
  </section>

  <p class="option-label option-label--3">FRONT OPTION 3</p>
  <p class="option-label option-label--4">OPTION 4</p>

</body>
</html>
```